Downtown hair salon need trendy website

I need a website with style. Unique. We need this site to list prices , Hair and nail services, service providers hours. I would also like my logo design on the website. We are located Downtown Grand rapids. Beautiful city with lots of culture.

Target Market(s)

Men and women

Industry/Entity Type

Hair And Beauty

Coding

Coded - Design and coding required

Number of Pages Required

3 page

Font styles to use
Sans Serif

Colors

Designer to choose colors to be used in the design.

Requirements
Must have
• Logo of business. Hours, services and prices, Page for pictures of each service provider. Nail service and prices. Products that we carry... Area on page for my mission statement.
Nice to have
• Pictures of trendy of the beauty industry. Men and women cuts.. Nails..
Should not have
• booking on line options...

```html
<!DOCTYPE html>
<html lang="en">
<head>
<meta charset="utf-8">
<title>Velora Salon Downtown</title>
<link rel="stylesheet" href="https://fonts.googleapis.com/css2?family=Playfair+Display:wght@700;900&family=Poppins:wght@400;500;600&display=swap">
<style>
:root{
  --gold:#b8862a;
  --gold-dark:#9c6f1e;
  --ink:#1e1e1e;
  --text:#6b6b6b;
  --muted:#e9e9e9;
  --band:#f1f1f1;
  --footer:#1a1a1a;
  --white:#ffffff;
}
*{box-sizing:border-box;margin:0;padding:0}
html,body{width:1200px;height:3680px;overflow:hidden}
body{font-family:"Poppins",sans-serif;color:var(--text);background:var(--white);position:relative}
.serif{font-family:"Playfair Display",serif}
.abs{position:absolute}
.btn{position:absolute;background:var(--gold);color:var(--white);font-size:11px;font-weight:600;letter-spacing:1px;
  text-transform:uppercase;border-radius:20px;display:flex;align-items:center;justify-content:center;height:30px}
.brand{display:flex;align-items:center;gap:10px;font-family:"Playfair Display",serif;font-weight:700;color:var(--gold);font-size:26px;letter-spacing:1px}
.brand .mark{width:16px;height:16px;background:var(--gold);border-radius:50%}

/* header */
.site-header{position:absolute;left:0;top:0;width:1200px;height:120px;background:var(--white)}
.site-header .brand{position:absolute;left:60px;top:44px}
.main-nav{position:absolute;right:160px;top:50px;display:flex;gap:26px;font-size:12px;font-weight:500;color:var(--ink);text-transform:uppercase}
.main-nav .active{color:var(--gold);border-bottom:2px solid var(--gold);padding-bottom:4px}
.search-icon{position:absolute;right:130px;top:50px}

/* hero */
.hero{position:absolute;left:0;top:120px;width:1200px;height:505px;
  background:linear-gradient(90deg,#c9c4c8 0%,#ddd6dc 35%,#eeeaee 60%,#f4f2f4 100%)}
.hero-photo{position:absolute;left:0;top:0;width:640px;height:505px;
  background:radial-gradient(ellipse at 45% 50%,#e7e2e6 0%,#c890b2 45%,#b9b3b8 80%)}
.hero-title{position:absolute;left:740px;top:120px;font-size:44px;font-weight:900;color:var(--ink);line-height:1.15;text-transform:uppercase}
.hero-text{position:absolute;left:740px;top:250px;width:360px;font-size:16px;color:var(--ink);line-height:1.3}
.hero .btn{left:900px;top:318px;width:120px}
.arrow{position:absolute;top:230px}
.dots{position:absolute;left:585px;top:470px;display:flex;gap:6px}
.dots span{width:8px;height:8px;border-radius:50%;background:#fff;opacity:.6}
.dots span.on{opacity:1}

/* section titles */
.eyebrow{position:absolute;width:1200px;text-align:center;color:var(--gold);font-family:"Playfair Display",serif;font-weight:700;font-size:18px}
.heading{position:absolute;width:1200px;text-align:center;color:var(--ink);font-family:"Playfair Display",serif;font-weight:900;font-size:32px}
.ghost{position:absolute;font-family:"Poppins",sans-serif;font-weight:600;font-size:92px;color:#000;opacity:.05;white-space:nowrap}

/* about */
.about{position:absolute;left:0;top:625px;width:1200px;height:625px;background:var(--white)}
.about-photo{position:absolute;left:170px;top:110px;width:330px;height:310px;background:linear-gradient(135deg,#f0f0f0,#c9c9c9 60%,#8a8580)}
.about-photo-inset{position:absolute;left:400px;top:250px;width:130px;height:140px;background:linear-gradient(135deg,#d8cfc6,#8b7e74);border:6px solid var(--white)}
.about-copy{position:absolute;left:640px;top:170px;width:340px}
.about-copy .eyebrow-left{color:var(--gold);font-family:"Playfair Display",serif;font-weight:700;font-size:18px}
.about-copy h2{font-family:"Playfair Display",serif;font-weight:900;font-size:32px;color:var(--ink);margin:4px 0 16px}
.about-copy p{font-size:11px;line-height:1.7;margin-bottom:12px}
.about .btn{left:640px;top:420px;width:130px}

/* services */
.services{position:absolute;left:0;top:1250px;width:1200px;height:710px;background:var(--band)}
.card{position:absolute;background:var(--white);width:275px;border-radius:6px;overflow:hidden;box-shadow:0 4px 14px rgba(0,0,0,.08)}
.card .photo{height:215px}
.card h3{font-family:"Playfair Display",serif;font-size:16px;color:var(--ink);margin:22px 22px 10px}
.card p{font-size:11px;line-height:1.7;margin:0 22px}
.card .more{font-size:12px;font-weight:600;color:var(--ink);margin:16px 22px}
.card.featured{background:var(--gold)}
.card.featured h3,.card.featured p,.card.featured .more{color:var(--white)}

/* gallery */
.gallery{position:absolute;left:0;top:1960px;width:1200px;height:760px;background:var(--white)}
.tile{position:absolute;width:275px;height:218px;border-radius:4px}

/* pricing */
.pricing{position:absolute;left:0;top:2720px;width:1200px;height:700px;background:var(--band)}
.price-card{position:absolute;top:175px;width:275px;height:435px;background:var(--white);border-radius:6px;box-shadow:0 4px 14px rgba(0,0,0,.08);text-align:center}
.price-card .photo{height:165px;border-radius:6px 6px 0 0}
.price-card .amount{font-family:"Playfair Display",serif;font-weight:900;font-size:34px;color:var(--ink);margin-top:18px}
.price-card .plan{font-size:13px;font-weight:600;color:var(--ink);margin-top:2px}
.price-card ul{list-style:none;font-size:11px;line-height:1.75;margin-top:14px}
.price-card .btn{left:87px;bottom:22px;width:100px}

/* footer */
.site-footer{position:absolute;left:0;top:3420px;width:1200px;height:260px;background:var(--footer);color:#cfcfcf}
.site-footer .brand{position:absolute;left:60px;top:80px}
.footer-col{position:absolute;top:40px;font-size:12px;line-height:1.9}
.footer-col h4{color:var(--white);font-size:14px;font-weight:600;margin-bottom:8px}
.footer-col .row{display:flex;align-items:center;gap:8px}
.footer-bottom{position:absolute;left:30px;right:30px;top:210px;border-top:1px solid #3a3a3a;padding-top:14px;font-size:11px}
.socials{position:absolute;right:30px;top:222px;display:flex;gap:8px}
.socials span{width:22px;height:22px;border-radius:50%;background:var(--white)}
</style>
</head>
<body>

<header class="site-header">
  <div class="brand"><span class="mark"></span>Velora Salon</div>
  <nav class="main-nav">
    <span class="active">Home</span><span>About</span><span>Services</span><span>Pricing</span><span>Contact Us</span>
  </nav>
  <svg class="search-icon" width="14" height="14" viewBox="0 0 14 14"><circle cx="6" cy="6" r="4.5" fill="none" stroke="#1e1e1e" stroke-width="1.6"/><line x1="9.3" y1="9.3" x2="13" y2="13" stroke="#1e1e1e" stroke-width="1.6"/></svg>
</header>

<section class="hero">
  <div class="hero-photo" role="img" aria-label="Woman with a silver and pink bob haircut"></div>
  <h1 class="hero-title serif">Velora Salon<br>Down Town</h1>
  <p class="hero-text">Lorem ipsum dolor sit amet, consectetur adipiscing elit, sed do eiusmod tempor.</p>
  <div class="btn">Contact Us</div>
  <svg class="arrow" style="left:20px" width="16" height="30" viewBox="0 0 16 30"><polyline points="13,2 3,15 13,28" fill="none" stroke="#fff" stroke-width="3"/></svg>
  <svg class="arrow" style="right:20px" width="16" height="30" viewBox="0 0 16 30"><polyline points="3,2 13,15 3,28" fill="none" stroke="#1e1e1e" stroke-width="3"/></svg>
  <div class="dots"><span class="on"></span><span></span><span></span></div>
</section>

<section class="about">
  <div class="ghost" style="left:-150px;top:250px;transform:rotate(-90deg)">About Us</div>
  <div class="about-photo" role="img" aria-label="Man with a styled short haircut"></div>
  <div class="about-photo-inset" role="img" aria-label="Barber trimming hair with scissors"></div>
  <div class="about-copy">
    <div class="eyebrow-left">About Us</div>
    <h2>Who We Are</h2>
    <p>Lorem ipsum dolor sit amet, consectetur adipiscing elit, sed do eiusmod tempor incididunt ut labore et dolore magna aliqua. Ut enim ad minim veniam, quis nostrud exercitation.</p>
    <p>Duis aute irure dolor in reprehenderit in voluptate velit esse cillum dolore eu fugiat nulla.</p>
  </div>
  <div class="btn">Read More</div>
</section>

<section class="services">
  <div class="ghost" style="left:1010px;top:300px;transform:rotate(-90deg)">Services</div>
  <div class="eyebrow" style="top:65px">Our Services</div>
  <div class="heading" style="top:88px">What We Do</div>

  <article class="card" style="left:170px;top:145px;height:445px">
    <div class="photo" role="img" aria-label="Barber giving a man a haircut" style="background:linear-gradient(135deg,#5a4a3e,#a08670)"></div>
    <h3>Mens Hair Cut</h3>
    <p>Lorem ipsum dolor sit amet, consectetur adipiscing elit, sed do eiusmod tempor incididunt ut labore.</p>
    <div class="more">Read More →</div>
  </article>
  <article class="card featured" style="left:462px;top:145px;height:445px">
    <div class="photo" role="img" aria-label="Woman with long styled auburn hair" style="background:linear-gradient(135deg,#6a4a32,#c99a6a)"></div>
    <h3>Women Hair Cut</h3>
    <p>Lorem ipsum dolor sit amet, consectetur adipiscing elit, sed do eiusmod tempor incididunt ut labore.</p>
    <div class="more">Read More →</div>
  </article>
  <article class="card" style="left:755px;top:145px;height:445px">
    <div class="photo" role="img" aria-label="Hands with teal manicured nails" style="background:linear-gradient(135deg,#e7c8bd,#7fb9b5)"></div>
    <h3>Nails Salon</h3>
    <p>Lorem ipsum dolor sit amet, consectetur adipiscing elit, sed do eiusmod tempor incididunt ut labore.</p>
    <div class="more">Read More →</div>
  </article>
  <div class="btn" style="left:540px;top:630px;width:120px">View All</div>
</section>

<section class="gallery">
  <div class="eyebrow" style="top:50px">Gallery</div>
  <div class="heading" style="top:72px;line-height:1.25">Check Out Our Latest<br>Work</div>
  <div class="tile" role="img" aria-label="Barber cutting a client's hair" style="left:15px;top:170px;background:linear-gradient(135deg,#3e3a36,#9c8a78)"></div>
  <div class="tile" role="img" aria-label="Stylist styling a woman's hair" style="left:312px;top:170px;background:linear-gradient(135deg,#8a7a6e,#d8cfc6)"></div>
  <div class="tile" role="img" aria-label="Manicure in progress" style="left:609px;top:170px;background:linear-gradient(135deg,#d9c2b6,#f2e8e2)"></div>
  <div class="tile" role="img" aria-label="Woman with styled long hair" style="left:906px;top:170px;background:linear-gradient(135deg,#b59a84,#efe3d8)"></div>
  <div class="tile" role="img" aria-label="Pedicure with red nail polish" style="left:15px;top:403px;background:linear-gradient(135deg,#e6c7b5,#b2412f)"></div>
  <div class="tile" role="img" aria-label="Man getting a barber haircut" style="left:312px;top:403px;background:linear-gradient(135deg,#2e2b2a,#8b7d72)"></div>
  <div class="tile" role="img" aria-label="Scissors trimming hair ends" style="left:609px;top:403px;background:linear-gradient(135deg,#b38a5c,#e8d3b4)"></div>
  <div class="tile" role="img" aria-label="Hands with pink manicured nails" style="left:906px;top:403px;background:linear-gradient(135deg,#f0d9d2,#d58b8a)"></div>
  <div class="btn" style="left:540px;top:665px;width:120px">View All</div>
</section>

<section class="pricing">
  <div class="ghost" style="left:1030px;top:310px;transform:rotate(-90deg)">Pricing</div>
  <div class="eyebrow" style="top:50px">Packages</div>
  <div class="heading" style="top:72px">Checkout Our Pricing</div>

  <article class="price-card" style="left:170px">
    <div class="photo" role="img" aria-label="Barber cutting a man's hair" style="background:linear-gradient(135deg,#6a5a4e,#c6b4a2)"></div>
    <div class="amount">$99.99</div>
    <div class="plan">Men Hair Cut</div>
    <ul><li>Wash and rinse</li><li>Classic fade cut</li><li>Beard line trim</li><li>Styling finish</li></ul>
    <div class="btn">View All</div>
  </article>
  <article class="price-card" style="left:462px">
    <div class="photo" role="img" aria-label="Stylist working on a woman's hair" style="background:linear-gradient(135deg,#7a6658,#d6c6b8)"></div>
    <div class="amount">$99.99</div>
    <div class="plan">Women Hair Cut</div>
    <ul><li>Wash and rinse</li><li>Layered cut</li><li>Blow dry style</li><li>Gloss finish</li></ul>
    <div class="btn">View All</div>
  </article>
  <article class="price-card" style="left:755px">
    <div class="photo" role="img" aria-label="Hands with red manicured nails" style="background:linear-gradient(135deg,#e9c9bf,#c2463e)"></div>
    <div class="amount">$99.99</div>
    <div class="plan">Nails</div>
    <ul><li>Nail shaping</li><li>Cuticle care</li><li>Gel polish</li><li>Hand massage</li></ul>
    <div class="btn">View All</div>
  </article>
</section>

<footer class="site-footer">
  <div class="brand"><span class="mark"></span>Velora Salon</div>
  <div class="footer-col" style="left:520px">
    <h4>Working Hours</h4>
    <div>Mon - Fri : 9am to 8pm</div>
    <div>Sat : 9am to 6pm</div>
    <div>Sunday : Closed</div>
  </div>
  <div class="footer-col" style="left:930px">
    <h4>Contact Us</h4>
    <div class="row"><svg width="12" height="12" viewBox="0 0 12 12"><path d="M2 1h3l1 3-1.5 1a7 7 0 0 0 2.5 2.5L8 6l3 1v3a1 1 0 0 1-1 1A9 9 0 0 1 1 2a1 1 0 0 1 1-1z" fill="var(--gold)"/></svg>(555) 010 2040</div>
    <div class="row"><svg width="12" height="12" viewBox="0 0 12 12"><rect x="0.5" y="2" width="11" height="8" fill="none" stroke="var(--gold)"/><polyline points="0.5,2 6,7 11.5,2" fill="none" stroke="var(--gold)"/></svg>hello@velorasalon.com</div>
    <div class="row"><svg width="12" height="12" viewBox="0 0 12 12"><path d="M6 11S2 6.5 2 4.5a4 4 0 0 1 8 0C10 6.5 6 11 6 11z" fill="var(--gold)"/><circle cx="6" cy="4.5" r="1.4" fill="#1a1a1a"/></svg>12 Maple Street, Downtown</div>
  </div>
  <div class="footer-bottom">Velora Salon Downtown © 2024. All Rights Reserved</div>
  <div class="socials"><span></span><span></span><span></span><span></span></div>
</footer>

</body>
</html>
```